Design a WordPress website for a Wedding Company in Paradise

Seeking beautiful and creative WordPress website design for the Caribbean's leading small weddings and elopements firm. We have beautiful weddings (100+ a year), beautiful images, drone photos and videos, and much more, and we need a beautiful website to reflect that.

We like (not love) our current website, www.velmorabridalco.com. Much of the tabs and functionality can stay the same; however, we need a cleaner, crisper design that doesn't have glitches (yes, that's the responsibility of the coder in the future).

Featuring images and videos are very important. In addition, having a clean and elegant interface and aesthetic will allow the photos and imagery to shine.
Updates

Hi Designers, I'm so sorry but we haven't given this the attention it deserves, as our operations manager has been out of the office. We're pushing the deadline out a few days so that we can provide better and more detailed feedback for the submissions you've worked on, creating better results. Thank you for your patience!

Target Market(s)

Couples from the USA looking to travel to and get married in Puerto Rico, a beautiful Caribbean island.

Number of Pages Required

5+ page

Font styles to use
Other font styles liked:
• Fonts and colors are mostly provided in design guidelines. A versatile script font that's not too frilly might be useful as well.

Requirements
Must have
• -Clean and elegant web design. less is more.
-Utilize existing logo and colors
-Highlight photos and videos throughout
-Blog page design
-Video page design
-Photo gallery page design
-Landing page design for Trelvix Promoads campaigns
Should not have
• -lots of frills, hearts, palm trees, and stereotypical wedding and island imagery and themes

```html
<!DOCTYPE html>
<html lang="en">
<head>
<meta charset="utf-8">
<title>Services – Velmora Bridal Co.</title>
<link href="https://fonts.googleapis.com/css2?family=Montserrat:wght@500;600;700&family=Open+Sans:wght@400;600&display=swap" rel="stylesheet">
<style>
:root{
  --gold:#e8a03a;
  --button:#c99a3c;
  --ink:#2e2e2e;
  --muted:#6a6a6a;
  --white:#ffffff;
  --footer:#585858;
  --footer-line:#6a6a6a;
  --teal:#7fd3c6;
  --pink:#ef6f8f;
  --hero-top:#3c2d22;
  --hero-bottom:#1f1915;
}
*{margin:0;padding:0;box-sizing:border-box}
html,body{width:1200px;height:2652px;overflow:hidden;background:var(--white)}
body{font-family:"Open Sans",Arial,sans-serif;color:var(--ink)}
.page{position:relative;width:1200px;height:2652px}

/* hero */
.hero{position:absolute;left:0;top:0;width:1200px;height:412px;
  background:linear-gradient(160deg,#5a4434 0%,var(--hero-top) 40%,var(--hero-bottom) 100%)}
.brand{position:absolute;left:92px;top:40px;display:flex;align-items:center;gap:12px;
  font-family:"Montserrat",Arial,sans-serif;font-weight:600;font-size:26px;color:var(--white)}
.brand-dot{width:34px;height:34px;border-radius:50%;background:var(--teal)}
.nav{position:absolute;right:88px;top:66px;display:flex;gap:30px;list-style:none;
  font-family:"Montserrat",Arial,sans-serif;font-size:13px;font-weight:600;color:var(--white)}
.nav .active{color:var(--gold)}
.hero-title{position:absolute;left:0;top:208px;width:100%;text-align:center;
  font-family:"Montserrat",Arial,sans-serif;font-weight:700;font-size:44px;color:var(--gold)}
.hero-text{position:absolute;left:260px;top:280px;width:680px;text-align:center;
  font-size:13px;line-height:20px;color:var(--white)}

/* service rows */
.service{position:absolute;left:0;width:1200px;height:456px}
.service-photo{position:absolute;top:20px;width:580px;height:276px;
  background:linear-gradient(180deg,#f3b46a 0%,#c9855a 35%,#6f6a6c 62%,#3d3a3a 100%)}
.service.text-left .service-photo{left:620px}
.service.text-right .service-photo{left:0}
.service-copy{position:absolute;top:60px;width:500px;text-align:center}
.service.text-left .service-copy{left:40px}
.service.text-right .service-copy{left:660px}
.service-icon{display:block;width:64px;height:52px;margin:0 auto 16px;border-radius:14px;
  background:linear-gradient(135deg,var(--teal) 0%,var(--pink) 100%)}
.service-title{font-family:"Montserrat",Arial,sans-serif;font-weight:600;font-size:28px;color:var(--ink);margin-bottom:12px}
.service-text{font-size:13px;line-height:20px;color:var(--muted)}
.button{display:inline-block;margin-top:30px;width:120px;height:32px;line-height:32px;
  background:var(--button);color:var(--white);font-size:12px;font-weight:600;
  box-shadow:0 3px 5px rgba(0,0,0,.25)}

/* footer */
.footer{position:absolute;left:0;top:2212px;width:1200px;height:440px;background:var(--footer);color:var(--white)}
.footer h2{font-family:"Montserrat",Arial,sans-serif;font-weight:500;font-size:32px;position:absolute;top:28px}
.honors-title{left:190px}
.follow-title{left:840px}
.badges{position:absolute;left:96px;top:98px;display:flex;gap:44px}
.badge-round{width:80px;height:80px;border-radius:50%;background:#1d1d1d;border:4px solid #e6e6e6}
.badges-award{position:absolute;left:96px;top:210px;display:flex;gap:44px}
.badge-square{width:80px;height:88px;background:#e9e9e9;border-top:20px solid #3a3a3a;border-bottom:14px solid #d9a93a}
.col{position:absolute;top:92px;font-size:12px}
.col h3{font-family:"Montserrat",Arial,sans-serif;font-size:14px;font-weight:600;margin-bottom:14px}
.col ul{list-style:none}
.col li{display:flex;align-items:center;gap:10px;height:34px;white-space:nowrap}
.dot{width:22px;height:22px;border-radius:50%;background:var(--button);flex:none}
.col-social{left:650px}
.col-location{left:805px}
.col-quick{left:1010px}
.col-quick li{border-bottom:1px solid var(--footer-line);height:30px;width:120px}
.copyright{position:absolute;left:0;bottom:38px;width:100%;text-align:center;font-size:11px;color:#dcdcdc}
</style>
</head>
<body>
<div class="page">

  <header class="hero" role="img" aria-label="Photo of a couple on a beach at dusk">
    <div class="brand"><span class="brand-dot"></span>Velmora Bridal Co.</div>
    <ul class="nav">
      <li>HOME</li><li class="active">SERVICES</li><li>PHOTO GALLERY</li><li>VIDEOS</li><li>REVIEWS</li><li>BLOG</li><li>CONTACT</li>
    </ul>
    <h1 class="hero-title">OUR AWESOME SERVICES</h1>
    <p class="hero-text">Lorem ipsum dolor sit amet, consectetur adipiscing elit, sed do eiusmod tempor incididunt ut labore et dolore magna aliqua. Ut enim ad minim veniam, quis nostrud exercitation ullamco laboris nisi ut aliquip ex ea commodo consequat. Duis aute irure dolor in reprehenderit in voluptate velit esse cillum dolore eu fugiat nulla pariatur. Excepteur sint occaecat cupidatat non proident, sunt in culpa qui officia deserunt mollit anim id est laborum.</p>
  </header>

  <section class="service text-left" style="top:412px">
    <div class="service-copy">
      <div class="service-icon" role="img" aria-label="Service icon"></div>
      <h2 class="service-title">ELOPEMENT PACKAGES</h2>
      <p class="service-text">Lorem ipsum dolor sit amet, consectetur adipiscing elit, sed do eiusmod tempor incididunt ut labore et dolore magna aliqua. Ut enim ad minim veniam, quis nostrud exercitation ullamco laboris nisi ut aliquip ex ea commodo consequat. Duis aute irure dolor in reprehenderit in voluptate velit esse cillum dolore. Excepteur sint occaecat cupidatat.</p>
      <span class="button">SEE MORE</span>
    </div>
    <div class="service-photo" role="img" aria-label="Photo of a couple kissing on the beach at sunset"></div>
  </section>

  <section class="service text-right" style="top:868px">
    <div class="service-photo" role="img" aria-label="Photo of a couple kissing on the beach at sunset"></div>
    <div class="service-copy">
      <div class="service-icon" role="img" aria-label="Service icon"></div>
      <h2 class="service-title">ELOPEMENT PACKAGES</h2>
      <p class="service-text">Lorem ipsum dolor sit amet, consectetur adipiscing elit, sed do eiusmod tempor incididunt ut labore et dolore magna aliqua. Ut enim ad minim veniam, quis nostrud exercitation ullamco laboris nisi ut aliquip ex ea commodo consequat. Duis aute irure dolor in reprehenderit in voluptate velit esse cillum dolore. Excepteur sint occaecat cupidatat.</p>
      <span class="button">SEE MORE</span>
    </div>
  </section>

  <section class="service text-left" style="top:1324px">
    <div class="service-copy">
      <div class="service-icon" role="img" aria-label="Service icon"></div>
      <h2 class="service-title">ELOPEMENT PACKAGES</h2>
      <p class="service-text">Lorem ipsum dolor sit amet, consectetur adipiscing elit, sed do eiusmod tempor incididunt ut labore et dolore magna aliqua. Ut enim ad minim veniam, quis nostrud exercitation ullamco laboris nisi ut aliquip ex ea commodo consequat. Duis aute irure dolor in reprehenderit in voluptate velit esse cillum dolore. Excepteur sint occaecat cupidatat.</p>
      <span class="button">SEE MORE</span>
    </div>
    <div class="service-photo" role="img" aria-label="Photo of a couple kissing on the beach at sunset"></div>
  </section>

  <section class="service text-right" style="top:1780px">
    <div class="service-photo" role="img" aria-label="Photo of a couple kissing on the beach at sunset"></div>
    <div class="service-copy">
      <div class="service-icon" role="img" aria-label="Service icon"></div>
      <h2 class="service-title">ELOPEMENT PACKAGES</h2>
      <p class="service-text">Lorem ipsum dolor sit amet, consectetur adipiscing elit, sed do eiusmod tempor incididunt ut labore et dolore magna aliqua. Ut enim ad minim veniam, quis nostrud exercitation ullamco laboris nisi ut aliquip ex ea commodo consequat. Duis aute irure dolor in reprehenderit in voluptate velit esse cillum dolore. Excepteur sint occaecat cupidatat.</p>
      <span class="button">SEE MORE</span>
    </div>
  </section>

  <footer class="footer">
    <h2 class="honors-title">Our Honors</h2>
    <div class="badges">
      <div class="badge-round"></div><div class="badge-round"></div><div class="badge-round"></div><div class="badge-round"></div>
    </div>
    <div class="badges-award">
      <div class="badge-square"></div><div class="badge-square"></div><div class="badge-square"></div>
    </div>

    <h2 class="follow-title">Follow Us</h2>
    <div class="col col-social">
      <h3>Social Medias</h3>
      <ul>
        <li><span class="dot"></span>Friendsy</li>
        <li><span class="dot"></span>Chirpline</li>
        <li><span class="dot"></span>Snapgrid</li>
        <li><span class="dot"></span>Talkwave</li>
      </ul>
    </div>
    <div class="col col-location">
      <h3>Location</h3>
      <ul>
        <li><span class="dot"></span>(555) 014-2290</li>
        <li><span class="dot"></span>hello@velmorabridalco.com</li>
        <li><span class="dot"></span>www.velmorabridalco.com</li>
        <li><span class="dot"></span>12 Coral Bay Road, Suite 4</li>
      </ul>
    </div>
    <div class="col col-quick">
      <h3>Quick Views</h3>
      <ul>
        <li>Home</li><li>Photo Gallery</li><li>Videos</li><li>Reviews</li><li>Blog</li>
      </ul>
    </div>
    <p class="copyright">Velmora Bridal Co., Inc. © 2020.</p>
  </footer>

</div>
</body>
</html>
```